Post Card Design Bright Lantern Youth

We need a postcard design that will be mailed to all residents offering free pickups of donated clothing. Our foundation is called Bright Lantern Youth, we are a nonprofit charitable organization that provides meals and medical services to children in need in Honduras. Collecting unwanted second-hand clothing generates revenue that helps fund the mission and programs run by our foundation. We would like to offer our pickup services to everyone who has any unwanted reusable clothing.

```html
<!DOCTYPE html>
<html lang="en">
<head>
<meta charset="utf-8">
<title>Bright Lantern Youth – Clothing Donation Postcard</title>
<link rel="stylesheet" href="https://fonts.googleapis.com/css2?family=Archivo+Black&family=Arimo:wght@400;700&family=Allura&display=swap">
<style>
  :root {
    --page: #ffffff;
    --card: #f7f5e2;
    --card-light: #fdfcf3;
    --ink: #343434;
    --green: #7cba3d;
    --panel: #d7e8a6;
    --rule: #c9c7b8;
    --frame: #8a8a84;
    --cloth-top: #9fb3c9;
    --cloth-bottom: #d9b48f;
  }
  * { box-sizing: border-box; margin: 0; padding: 0; }
  html, body { width: 1200px; height: 1000px; overflow: hidden; background: var(--page); }
  body { position: relative; font-family: "Arimo", Arial, sans-serif; color: var(--ink); }

  .card {
    position: absolute; left: 315px; width: 532px; height: 356px;
    background: radial-gradient(ellipse at 40% 45%, var(--card-light) 0%, var(--card) 70%);
    box-shadow: 3px 4px 6px rgba(0,0,0,0.12);
  }
  .card--front { top: 101px; }
  .card--back { top: 505px; }

  /* Front */
  .headline { position: absolute; left: 57px; top: 62px; z-index: 2; font-family: "Archivo Black", Arial, sans-serif; font-weight: 400; line-height: 1; text-transform: uppercase; white-space: nowrap; }
  .headline > div { transform-origin: left top; }
  .headline__line1 { font-size: 37px; letter-spacing: -0.5px; transform: scaleX(0.92); }
  .headline__line2 { font-size: 69px; color: var(--green); letter-spacing: -2px; margin-top: -2px; transform: scale(0.92, 0.9); }
  .headline__line3 { font-size: 34px; margin-top: -7px; letter-spacing: -0.3px; transform: scaleX(0.86); }
  .accent { color: var(--green); }

  .clothing-photo {
    position: absolute; left: 335px; top: 144px; width: 90px; height: 86px; border-radius: 6px; z-index: 1;
    background: linear-gradient(180deg, var(--cloth-top) 0%, #c9cfd6 50%, var(--cloth-bottom) 100%);
  }

  .tagline { position: absolute; right: 120px; top: 292px; text-align: right; font-weight: 700; text-transform: uppercase; line-height: 1.05; }
  .tagline__main { font-size: 15px; }
  .tagline__sub { font-size: 13px; }
  .tagline__call { font-size: 9px; margin-top: 2px; }

  .brand-name { font-family: "Arimo", Arial, sans-serif; font-weight: 700; color: var(--green); line-height: 1.1; }
  .card--front .brand-name { position: absolute; left: 424px; top: 290px; width: 90px; font-size: 13px; text-align: center; }
  .brand-dot { display: block; width: 16px; height: 16px; border-radius: 50%; background: var(--green); margin: 0 auto 5px; }

  /* Back */
  .card--back .brand-name { position: absolute; left: 36px; top: 40px; width: 110px; font-size: 15px; }
  .about-frame { position: absolute; left: 23px; top: 100px; width: 252px; height: 213px; border: 1px solid var(--frame); }
  .about {
    position: absolute; left: 27px; top: 103px; width: 245px; height: 207px;
    background: var(--panel); padding: 10px 10px 0 9px; font-size: 12px; line-height: 14.3px;
  }
  .about p.justify { text-align: justify; }

  .stamp { position: absolute; left: 442px; top: 35px; width: 68px; height: 67px; border: 1px solid var(--ink); }
  .address-line { position: absolute; left: 299px; width: 211px; border-top: 1px dashed var(--rule); }
  .note {
    position: absolute; left: 296px; top: 174px; width: 230px;
    font-family: "Allura", cursive; font-size: 19px; line-height: 24px; color: var(--ink);
  }
  .contact { position: absolute; left: 298px; top: 247px; list-style: none; font-size: 12.5px; }
  .contact li { display: flex; align-items: center; height: 22px; }
  .contact svg { width: 14px; height: 14px; margin-right: 7px; fill: var(--green); }
</style>
</head>
<body>

<section class="card card--front">
  <h1 class="headline">
    <div class="headline__line1">Share your <span class="accent">used</span></div>
    <div class="headline__line2">Clothing</div>
    <div class="headline__line3">For the needy</div>
  </h1>
  <div class="clothing-photo" role="img" aria-label="Stack of folded donated clothes tied with a string"></div>
  <div class="tagline">
    <div class="tagline__main">Used clothing</div>
    <div class="tagline__sub">Also saves lives</div>
    <div class="tagline__call">Call 555-0148 and donate</div>
  </div>
  <div class="brand-name"><span class="brand-dot"></span>Bright Lantern Youth</div>
</section>

<section class="card card--back">
  <div class="brand-name">Bright Lantern Youth</div>
  <div class="about-frame"></div>
  <div class="about">
    <p>We are a nonprofit charitable organization that provides meals and medical services to children in need in Honduras.</p>
    <p>We are a nonprofit charitable organization that provides meals and medical services to children in need in Honduras.</p>
    <p class="justify">Collecting unwanted second-hand clothing generates revenue that helps fund the mission and programs run by our foundation.</p>
    <p>We would like to offer our pickup services to everyone who has any unwanted reusable clothing.</p>
  </div>

  <div class="stamp"></div>
  <div class="address-line" style="top:135px"></div>
  <div class="address-line" style="top:157px"></div>
  <div class="address-line" style="top:200px"></div>
  <div class="address-line" style="top:222px"></div>
  <p class="note">Please bring used clothing to share<br>the warmth with the needy</p>

  <ul class="contact">
    <li><svg viewBox="0 0 24 24"><path d="M12 2a7 7 0 0 0-7 7c0 5 7 13 7 13s7-8 7-13a7 7 0 0 0-7-7zm0 9.5A2.5 2.5 0 1 1 12 6.5a2.5 2.5 0 0 1 0 5z"/></svg>18 Mill Creek Rd, Oakdale, NJ 07990</li>
    <li><svg viewBox="0 0 24 24"><path d="M6.6 10.8a15 15 0 0 0 6.6 6.6l2.2-2.2c.3-.3.7-.4 1-.2 1.1.4 2.3.6 3.6.6.6 0 1 .4 1 1V20c0 .6-.4 1-1 1A17 17 0 0 1 3 4c0-.6.4-1 1-1h3.5c.6 0 1 .4 1 1 0 1.3.2 2.5.6 3.6.1.3 0 .7-.2 1z"/></svg>(201) 555-0148</li>
    <li><svg viewBox="0 0 24 24"><path d="M2 5h20v14H2z M2 5l10 7 10-7" /></svg>info@brightlanternyouth.org</li>
  </ul>
</section>

</body>
</html>
```